dsadasdasdasdsa

Industry/Entity Type

Mortgage Broking

Requirements
Must have
• Call-to-action button somewhere on the graphic
Nice to have
• The font of our logo is Montserrat

```html
<!DOCTYPE html>
<html lang="en">
<head>
<meta charset="UTF-8">
<title>Need a Mortgage Broker? Banner</title>
<link href="https://fonts.googleapis.com/css2?family=Archivo:wght@900&family=Roboto+Condensed:wght@700&display=swap" rel="stylesheet">
<style>
  :root {
    --page-bg: #ffffff;
    --band-green: #8fcaa6;
    --band-light: #eef0f0;
    --headline-green: #1d5535;
    --cta-red: #c63f2f;
    --cta-text: #ffffff;
    --mascot-green: #5fbf5a;
    --mascot-shell: #8a5a3a;
  }
  html, body {
    margin: 0;
    padding: 0;
    width: 1200px;
    height: 957px;
    overflow: hidden;
    background: var(--page-bg);
  }
  .canvas {
    position: relative;
    width: 1200px;
    height: 957px;
  }
  .broker-banner {
    position: absolute;
    left: 36px;
    top: 390px;
    width: 1128px;
    height: 176px;
    overflow: hidden;
    background: linear-gradient(90deg,
      var(--band-green) 0%,
      #c9e2d2 12%,
      var(--band-light) 30%,
      var(--band-light) 70%,
      #c9e2d2 86%,
      var(--band-green) 100%);
  }
  .mascot {
    position: absolute;
    border-radius: 46% 46% 10% 10%;
  }
  .mascot--waving {
    left: 34px;
    top: 6px;
    width: 190px;
    height: 170px;
    background: radial-gradient(ellipse at 50% 40%, var(--mascot-green) 0%, #4aa94a 55%, var(--mascot-shell) 100%);
  }
  .mascot--house {
    left: 930px;
    top: 4px;
    width: 130px;
    height: 172px;
    background: radial-gradient(ellipse at 45% 35%, var(--mascot-green) 0%, #4aa94a 50%, var(--mascot-shell) 100%);
  }
  .headline {
    position: absolute;
    left: 0;
    right: 0;
    top: 26px;
    margin: 0;
    text-align: center;
    white-space: nowrap;
    font-family: "Archivo", Arial, sans-serif;
    font-weight: 900;
    font-size: 37px;
    line-height: 46px;
    letter-spacing: 1px;
    color: var(--headline-green);
  }
  .cta-button {
    position: absolute;
    left: 298px;
    top: 88px;
    width: 552px;
    height: 50px;
    border-radius: 7px;
    background: var(--cta-red);
    color: var(--cta-text);
    display: flex;
    align-items: center;
    justify-content: center;
    white-space: nowrap;
    font-family: "Roboto Condensed", "Arial Narrow", sans-serif;
    font-weight: 700;
    font-size: 26px;
    line-height: 1;
    letter-spacing: 1.2px;
    text-decoration: none;
  }
</style>
</head>
<body>
<div class="canvas">
  <section class="broker-banner">
    <div class="mascot mascot--waving" role="img" aria-label="Smiling cartoon turtle mascot peeking in from the left"></div>
    <h1 class="headline">Need a Mortgage Broker?</h1>
    <a class="cta-button" href="#">Search Now on Australia's Largest Directory</a>
    <div class="mascot mascot--house" role="img" aria-label="Cartoon turtle mascot standing and holding a small house"></div>
  </section>
</div>
</body>
</html>
```